Purple Heart Veteran Owned Telecommunications Company

I need to develop my current website (corvalbrook.com) into something more upbeat and modern. I created the existing one with NestPlank and it's very basic. I'm open to using any type of website builder and not just NestPlank. I feel like NestPlank is pretty basic. I want something customized to me and my company. I plan on doing a Zintora Ad, Email Marketing, and Mail Marketing campaign and SEO push. I want a website built so they can look up my company. We are a low voltage telecommunications company based out of Harlow Bay. We are a General Contractor and I have technicians all throughout the US and Canada. I mainly appeal to the government and fortune 500 companies across the country. I focus on commercial and federal work with minor work in Residential. I need to appeal to everyone and not just locally. My company name is Corvalbrook. I'm a Marine Corps veteran and my I created the company with my son in mind. We are a service disabled veteran owned small business. I'm open to any play on my logo or color scheme. I do like the color blue but I'm open to anything again. I would like a website that has little maintenance needed and something that is modern and sticks out with my competitors. I'm only in business for 2 years but I need to stick out to my competition so I can start building revenue through ads and getting my name out there with limited funds. I did have a logo and name created which I'm attaching. I'm completely open to changing it if someone can come up with something creative. I would like someone that understands SEO and can help feed work to my site. I'm also open to paying more for the right website that gets everything I want. I know I need to add more pages and more professional. Please use my website as a template but also feel free to come up with any new ideas. I would like some feedback or ideas on what else to add to my website or remove so I can appeal to my audience and look more authentic.

Target Market(s)

Commercial Companies locally in Harlow Bay, and Fortune 500 companies and the government

Industry/Entity Type

Telecommunications

Coding

Coded - Design and coding required

Number of Pages Required

5+ page

Font styles to use
Sans Serif

Requirements
Must have
• A Modern, fresh look that is customized and original. Something that sticks out to my customers.
Nice to have
• Anything that sticks out and isn't stock. I'm open to anything that is unique and different.
Should not have
• Nothing Generic. I would like something custom tailored to my business

```html
<!DOCTYPE html>
<html lang="en">
<head>
<meta charset="utf-8">
<title>Corvalbrook — Low Voltage Telecommunications</title>
<link href="https://fonts.googleapis.com/css2?family=Mulish:wght@400;600;700;800&display=swap" rel="stylesheet">
<style>
:root{
  --navy:#16245a;
  --deep:#0c1533;
  --ink:#1c2440;
  --blue:#1f3a93;
  --accent:#2d55c4;
  --grey:#6b6f78;
  --light:#eef1f7;
  --white:#ffffff;
}
*{box-sizing:border-box;margin:0;padding:0}
html,body{width:1200px;height:4656px;overflow:hidden}
body{font-family:"Mulish",Arial,sans-serif;color:var(--ink);background:var(--white);position:relative}
section,header,footer{position:absolute;left:0;width:1200px}
.btn{display:inline-block;background:var(--white);color:var(--navy);font-weight:700;font-size:15px;padding:9px 20px;border-radius:3px}

/* header */
.site-header{top:0;height:80px;background:var(--white);box-shadow:0 2px 8px rgba(0,0,0,.08);z-index:5}
.brand{position:absolute;left:150px;top:18px;display:flex;align-items:center;gap:10px}
.brand-dot{width:30px;height:30px;border-radius:50%;background:var(--navy)}
.brand-name{font-weight:800;font-size:17px;letter-spacing:1px;color:var(--navy)}
.main-nav{position:absolute;left:540px;top:22px;display:flex;gap:50px;font-size:15px;color:var(--grey)}
.main-nav .active{color:var(--navy);font-weight:700;border-bottom:2px solid var(--navy);padding-bottom:6px}

/* hero */
.hero{top:80px;height:600px;background:linear-gradient(120deg,#0c1a4a 0%,#1b3a90 55%,#0d1b48 100%);clip-path:polygon(0 0,100% 0,100% 78%,0 100%)}
.hero-photo{position:absolute;left:430px;top:20px;width:420px;height:500px;background:linear-gradient(160deg,#3a5fc0,#1a2f78 60%,#0e1b4c);clip-path:polygon(0 8%,100% 8%,50% 100%)}
.hero-text{position:absolute;left:150px;top:190px;color:var(--white)}
.hero-text .kicker{font-size:20px;font-weight:600}
.hero-text .kicker b{font-weight:800}
.hero-text h1{font-size:44px;font-weight:800;letter-spacing:.5px;line-height:1.05;margin:4px 0 6px}
.hero-text p{font-size:22px;font-weight:700;line-height:1.25;margin-bottom:22px}
.slider-dot{position:absolute;left:1032px;top:270px;width:10px;height:10px;border-radius:50%;background:var(--white)}

/* features */
.features{top:690px;height:400px}
.hex{position:absolute;top:0;width:230px;height:210px}
.feature{position:absolute;top:240px;width:200px;text-align:center}
.feature h3{font-size:18px;font-weight:800;color:var(--navy);margin-bottom:8px}
.feature p{font-size:14px;line-height:1.35;color:var(--grey)}
.chev{display:block;margin:8px auto 0;width:14px;height:8px}

/* why */
.why{top:1120px;height:500px;background:linear-gradient(90deg,#0c1533,#1a2a62);clip-path:polygon(0 14%,100% 0,100% 86%,0 100%)}
.why-text{position:absolute;left:150px;top:150px;color:var(--white)}
.why-text h2{font-size:42px;font-weight:800;margin-bottom:24px}
.why-text p{font-size:19px;line-height:1.6}
.why-photo-a{position:absolute;left:560px;top:70px;width:260px;height:330px;background:linear-gradient(150deg,#9fb3d8,#3b5596);clip-path:polygon(0 0,100% 0,50% 100%)}
.why-photo-b{position:absolute;left:700px;top:90px;width:340px;height:310px;background:linear-gradient(140deg,#2a2a30,#6e5a3a 55%,#1a1a1f);clip-path:polygon(40% 0,100% 0,100% 100%,0 100%)}

/* services */
.services{top:1700px;height:680px}
.section-title{text-align:center;font-size:34px;font-weight:800;color:var(--navy)}
.services .section-title{position:absolute;top:70px;width:100%}
.service{position:absolute;top:150px;width:240px}
.service-frame{position:absolute;left:30px;top:0;width:180px;height:180px;border:5px solid var(--navy)}
.service-photo{position:absolute;left:0;top:30px;width:240px;height:230px;clip-path:polygon(0 0,100% 0,50% 100%)}
.service ul{position:absolute;top:285px;left:0;width:240px;list-style:none;font-size:15px;color:var(--grey);text-align:center;line-height:1.35}
.service li{margin-bottom:10px}
.service li::before{content:"✓ ";color:var(--navy)}

/* markets */
.markets{top:2400px;height:680px;background:linear-gradient(180deg,#1c2a5e,#15214c)}
.markets .section-title{position:absolute;top:55px;width:100%;color:var(--white)}
.market-tabs{position:absolute;top:122px;width:100%;text-align:center;color:var(--white);font-size:18px;font-weight:700}
.market-tabs span{margin:0 16px}
.tile{position:absolute;top:250px;height:300px}
.tile-center{top:200px;height:350px;border:4px solid #8fd4e6}
.arrow{position:absolute;top:210px;width:38px;height:38px;border-radius:50%;background:var(--white)}
.view-all{position:absolute;top:584px;left:550px;background:var(--white);color:var(--navy);font-weight:700;font-size:14px;padding:9px 26px;border-radius:3px}

/* team */
.team{top:3080px;height:520px}
.team .section-title{position:absolute;top:80px;width:100%}
.circle{position:absolute;border-radius:50%;display:flex;flex-direction:column;align-items:center;justify-content:center;color:var(--white);font-weight:800;font-size:18px;text-align:center;line-height:1.3}
.circle-blue{top:170px;width:250px;height:250px;background:var(--navy)}
.circle-grey{top:140px;left:445px;width:310px;height:310px;background:radial-gradient(circle,#7a7a7a,#3c3c3c)}
.badge{width:80px;height:80px;border-radius:50%;border:3px solid var(--white);margin-bottom:18px}
.icon-ring{width:80px;height:80px;border-radius:50%;background:var(--white);margin-bottom:16px;display:flex;align-items:center;justify-content:center}

/* references */
.references{top:3600px;height:560px;background:linear-gradient(110deg,#0d1638,#1d3478 60%,#0e1a44);clip-path:polygon(0 10%,100% 0,100% 100%,0 100%)}
.ref-text{position:absolute;left:150px;top:150px;color:var(--white)}
.ref-text h2{font-size:46px;font-weight:800;margin-bottom:18px}
.ref-text p{font-size:17px;line-height:1.5;margin-bottom:26px}
.ref-person{position:absolute;left:700px;top:40px;width:300px;height:520px;background:linear-gradient(180deg,#f1b81f 0%,#f1b81f 12%,#d6ad8f 22%,#e9e9ea 40%,#3a3f4a 100%);border-radius:140px 140px 0 0}

/* footer */
.site-footer{top:4120px;height:536px;background:var(--deep);color:var(--white)}
.footer-brand{position:absolute;left:150px;top:80px;width:260px}
.footer-brand .brand-name{color:var(--white);display:block;margin-top:8px}
.footer-brand .brand-dot{background:var(--white);margin-left:40px}
.footer-brand p{font-size:14px;line-height:1.45;margin-top:14px;color:#d5daea}
.footer-col{position:absolute;top:75px}
.footer-col h4{font-size:16px;font-weight:700;margin-bottom:20px}
.footer-col li{list-style:none;font-size:14px;margin-bottom:14px;display:flex;align-items:center;gap:8px}
.field{width:200px;height:30px;background:var(--white);border-radius:2px;margin-bottom:8px;color:#999;font-size:12px;padding:7px 10px}
.field.tall{height:70px}
.submit{display:inline-block;background:var(--white);color:var(--navy);font-size:13px;font-weight:700;padding:6px 18px;margin-top:4px}
.copyright{position:absolute;left:150px;top:478px;font-size:14px;color:#d5daea}
</style>
</head>
<body>

<header class="site-header">
  <div class="brand"><span class="brand-dot"></span><span class="brand-name">CORVALBROOK</span></div>
  <nav class="main-nav">
    <span class="active">Home</span><span>Low Voltage</span><span>Markets</span><span>Our Team</span><span>Contact Us</span>
  </nav>
</header>

<section class="hero">
  <div class="hero-photo" role="img" aria-label="Technician in a hard hat at a network installation"></div>
  <div class="hero-text">
    <div class="kicker">WE ARE A <b>LOW VOLTAGE</b></div>
    <h1>TELECOMMUNICATIONS<br>COMPANY</h1>
    <p>With Over 20 Years Of<br>Proven Experience</p>
    <span class="btn">Learn More</span>
  </div>
  <span class="slider-dot"></span>
</section>

<section class="features">
  <svg class="hex" style="left:285px" viewBox="0 0 230 210"><polygon points="58,5 172,5 225,105 172,205 58,205 5,105" fill="none" stroke="#1f3a93" stroke-width="10"/><g fill="none" stroke="#1f3a93" stroke-width="4"><circle cx="115" cy="95" r="22"/><path d="M105 117v14h20v-14M115 55v10M80 95h10M140 95h10M90 70l7 7M140 70l-7 7"/></g></svg>
  <svg class="hex" style="left:485px" viewBox="0 0 230 210"><polygon points="58,5 172,5 225,105 172,205 58,205 5,105" fill="none" stroke="#1f3a93" stroke-width="10"/><g fill="none" stroke="#1f3a93" stroke-width="4"><path d="M80 100l20-20 15 10 15-10 20 20-35 30z"/><path d="M100 105l10 8M108 98l12 10"/></g></svg>
  <svg class="hex" style="left:685px" viewBox="0 0 230 210"><polygon points="58,5 172,5 225,105 172,205 58,205 5,105" fill="none" stroke="#1f3a93" stroke-width="10"/><g fill="none" stroke="#1f3a93" stroke-width="4"><path d="M115 100c-14-12-24-20-14-30 6-5 12-2 14 3 2-5 8-8 14-3 10 10 0 18-14 30z"/><path d="M80 95v30l20 15M150 95v30l-20 15"/></g></svg>
  <div class="feature" style="left:300px"><h3>What We Do</h3><p>Our past projects include both new construction and repairs/alterations. Occupied...</p><svg class="chev" viewBox="0 0 14 8"><path d="M1 1l6 6 6-6" fill="none" stroke="#16245a" stroke-width="2"/></svg></div>
  <div class="feature" style="left:500px"><h3>Working Together</h3><p>We offer an end-to-end client experience that includes seamless communication...</p><svg class="chev" viewBox="0 0 14 8"><path d="M1 1l6 6 6-6" fill="none" stroke="#16245a" stroke-width="2"/></svg></div>
  <div class="feature" style="left:700px"><h3>Trust</h3><p>We are committed to building trust among our clients, contractors, colleagues, and community.</p><svg class="chev" viewBox="0 0 14 8"><path d="M1 1l6 6 6-6" fill="none" stroke="#16245a" stroke-width="2"/></svg></div>
</section>

<section class="why">
  <div class="why-text">
    <h2>Why Choose Us</h2>
    <p>Do you have an emergency service call?<br>Do you need help installing your security system?<br>Do you have a 2,000 site nationwide roll-out?</p>
  </div>
  <div class="why-photo-b" role="img" aria-label="Hand holding a glowing light bulb"></div>
  <div class="why-photo-a" role="img" aria-label="Smiling technician in a hard hat"></div>
</section>

<section class="services">
  <h2 class="section-title">Services</h2>
  <div class="service" style="left:200px">
    <div class="service-frame"></div>
    <div class="service-photo" role="img" aria-label="Technician wiring a network rack" style="background:linear-gradient(160deg,#9cc0e6,#5a6f8f)"></div>
    <ul><li>Low Voltage Wiring and Cabling</li><li>Voice and Data Network Cabling</li><li>CAT 5/6, Fiber Optic, and Coax Cabling</li><li>Single and Multiple Floor Installations</li></ul>
  </div>
  <div class="service" style="left:480px">
    <div class="service-frame"></div>
    <div class="service-photo" role="img" aria-label="Server room with network cables" style="background:linear-gradient(160deg,#2a3040,#6b7fa5 60%,#c9a3b8)"></div>
    <ul><li>Server Racks/ Networking Setup</li><li>Audio/Video Cabling and Wiring</li><li>WiFi – Wireless Network Installation</li><li>Access Point Installation</li></ul>
  </div>
  <div class="service" style="left:760px">
    <div class="service-frame"></div>
    <div class="service-photo" role="img" aria-label="Security camera being installed" style="background:linear-gradient(160deg,#e6e3df,#a9a7a5 60%,#6b6b6b)"></div>
    <ul><li>Voice &amp; Telephone Wiring</li><li>Demarc Extension</li><li>Security Camera Installation</li><li>Heat Mapping</li></ul>
  </div>
</section>

<section class="markets">
  <h2 class="section-title">Markets</h2>
  <div class="market-tabs"><span>Commercial</span>|<span>Residential</span></div>
  <div class="tile" style="left:0;width:200px;background:linear-gradient(180deg,#d8a25a,#7a5a3a)" role="img" aria-label="Office towers at sunset"></div>
  <div class="tile" style="left:210px;width:240px;background:linear-gradient(180deg,#2a2350,#b8546d 60%,#e0a060)" role="img" aria-label="City skyline at night"></div>
  <div class="tile tile-center" style="left:475px;width:250px;background:linear-gradient(180deg,#0e2a3a,#3aa7c4 60%,#12384a)" role="img" aria-label="Data center server aisle"></div>
  <div class="tile" style="left:730px;width:230px;background:radial-gradient(circle at 50% 40%,#f0b868,#3a2a1a 60%,#1a140e)" role="img" aria-label="Glowing light bulb"></div>
  <div class="tile" style="left:965px;width:235px;background:linear-gradient(180deg,#a9c6e0,#4f6f92)" role="img" aria-label="Modern glass office building"></div>
  <svg class="arrow" style="left:322px" viewBox="0 0 38 38"><circle cx="19" cy="19" r="19" fill="#fff"/><path d="M22 12l-7 7 7 7" fill="none" stroke="#16245a" stroke-width="3"/></svg>
  <svg class="arrow" style="left:830px" viewBox="0 0 38 38"><circle cx="19" cy="19" r="19" fill="#fff"/><path d="M16 12l7 7-7 7" fill="none" stroke="#16245a" stroke-width="3"/></svg>
  <span class="view-all">View All</span>
</section>

<section class="team">
  <h2 class="section-title">Our Team</h2>
  <div class="circle circle-blue" style="left:180px"><span class="badge"></span>Veteran Owned<br>(SDVOSB)</div>
  <div class="circle circle-grey"><span class="icon-ring"><svg width="44" height="44" viewBox="0 0 44 44"><circle cx="19" cy="19" r="12" fill="none" stroke="#16245a" stroke-width="4"/><path d="M28 28l12 12" stroke="#16245a" stroke-width="5"/></svg></span>Hiring Veterans</div>
  <div class="circle circle-blue" style="left:770px"><span class="icon-ring"><svg width="40" height="44" viewBox="0 0 40 44"><rect x="6" y="4" width="28" height="36" fill="none" stroke="#16245a" stroke-width="3"/><path d="M12 14h16M12 21h16M12 28h10" stroke="#16245a" stroke-width="3"/></svg></span>National Team of<br>Contractors</div>
</section>

<section class="references">
  <div class="ref-text">
    <h2>Want References?</h2>
    <p>Ask us! We can provide commercial and federal<br>references! We take pride in our transparency!</p>
    <span class="btn">Learn More</span>
  </div>
  <div class="ref-person" role="img" aria-label="Contractor in a yellow hard hat with arms crossed"></div>
</section>

<footer class="site-footer">
  <div class="footer-brand">
    <span class="brand-dot" style="display:block"></span>
    <span class="brand-name">CORVALBROOK</span>
    <p>Our past projects include both new construction and repairs/alterations. Occupied and fully operational job sites are never a problem. And we can also plan, manage.</p>
  </div>
  <div class="footer-col" style="left:460px"><h4>Quick Link</h4><ul><li>Home</li><li>Low Voltage</li><li>Markets</li><li>Our Team</li><li>Contact Us</li></ul></div>
  <div class="footer-col" style="left:600px"><h4>Contact</h4><ul><li>☎ 555-014-2730</li><li>✉ support@corvalbrook.com</li><li>⌖ Harlow Bay</li></ul></div>
  <div class="footer-col" style="left:830px"><h4>Get in Touch</h4>
    <div class="field">Name</div><div class="field">Email</div><div class="field">Ph no.</div><div class="field tall">Message</div><span class="submit">Submit</span>
  </div>
  <p class="copyright">Copyright©2021corvalbrook . All Rights Reserved.</p>
</footer>

</body>
</html>
```